App Design for a petrol price in Nigeria

Through your already existing prototypes, we intend to design an app that would show petrol prices in Nigeria. The app would enable the user monitor the prices of petrol products in real time from nearby stations.

Industry/Entity Type

Gas And Oil

Requirements
Must have
• User community (sign up) and crowdsourced database integration

```html
<!DOCTYPE html>
<html lang="en">
<head>
<meta charset="utf-8">
<title>Settings</title>
<link href="https://fonts.googleapis.com/css2?family=Inter:wght@700&family=Nunito+Sans:wght@400;600;700&display=swap" rel="stylesheet">
<style>
:root{
  --brand:#007aff;
  --white:#ffffff;
  --ink:#111111;
  --label:#333333;
  --muted:#555555;
  --rule:#e2e2e2;
  --on:#4cd964;
  --track-off:#e6e6e6;
}
*{margin:0;padding:0;box-sizing:border-box}
html,body{width:1200px;height:2596px;overflow:hidden;background:var(--white)}
body{position:relative;font-family:"Nunito Sans",sans-serif}
.app-header{position:absolute;left:0;top:0;width:1200px;height:355px;background:var(--brand);border-radius:0 0 110px 110px}
.status-time{position:absolute;left:104px;top:44px;color:var(--white);font:700 48px "Inter",sans-serif}
.status-icons{position:absolute;right:44px;top:52px}
.page-title{position:absolute;left:0;width:1200px;top:200px;text-align:center;color:var(--white);font:700 76px "Inter",sans-serif}
.settings-card{position:absolute;left:72px;top:446px;width:1056px;height:1302px;background:var(--white);border-radius:110px;box-shadow:0 0 22px rgba(0,0,0,.06)}
.card-title{position:absolute;left:0;width:100%;top:72px;text-align:center;color:var(--ink);font-size:54px;font-weight:400}
.setting-row{position:absolute;left:106px;width:850px;border-bottom:2px solid var(--rule)}
.setting-label{font-size:46px;color:var(--label);display:block}
.setting-hint{font-size:33px;color:var(--muted);display:block;margin-top:10px}
.toggle{position:absolute;right:0;width:148px;height:90px;border-radius:45px}
.toggle::after{content:"";position:absolute;top:3px;width:84px;height:84px;border-radius:50%;background:var(--white);box-shadow:0 3px 6px rgba(0,0,0,.3)}
.toggle.is-on{background:var(--on)}
.toggle.is-on::after{right:3px}
.toggle.is-off{background:var(--white);border:3px solid var(--track-off)}
.toggle.is-off::after{left:0;top:0}
.back-button{position:absolute;left:257px;top:1018px;width:556px;height:160px;border-radius:80px;background:var(--brand);color:var(--white);display:flex;align-items:center;justify-content:center;gap:36px;font:700 58px "Nunito Sans",sans-serif}
.tab-bar{position:absolute;left:0;top:2374px;width:1200px;height:222px;background:var(--brand);border-radius:110px 110px 0 0}
.tab{position:absolute;top:80px}
.tab-active{position:absolute;left:843px;top:58px;width:316px;height:116px;border-radius:58px;background:var(--white);display:flex;align-items:center;justify-content:center;gap:16px;color:var(--brand);font-size:46px;font-weight:600}
</style>
</head>
<body>
<header class="app-header">
  <span class="status-time">9:41</span>
  <svg class="status-icons" width="212" height="40" viewBox="0 0 212 40" fill="#fff">
    <rect x="0" y="26" width="9" height="12" rx="2"/><rect x="14" y="20" width="9" height="18" rx="2"/><rect x="28" y="12" width="9" height="26" rx="2"/><rect x="42" y="4" width="9" height="34" rx="2"/>
    <path d="M90 36l-8-9a12 12 0 0 1 16 0z M71 18a27 27 0 0 1 38 0l-5 5a20 20 0 0 0-28 0z M62 9a40 40 0 0 1 56 0l-5 5a33 33 0 0 0-46 0z"/>
    <rect x="135" y="2" width="70" height="34" rx="9" fill="none" stroke="#fff" stroke-width="3" opacity=".7"/>
    <rect x="140" y="7" width="60" height="24" rx="5"/><rect x="207" y="13" width="4" height="12" rx="2" opacity=".7"/>
  </svg>
  <h1 class="page-title">Settings</h1>
</header>

<main class="settings-card">
  <h2 class="card-title">Push Notifications</h2>
  <div class="setting-row" style="top:236px;height:154px;padding-top:20px">
    <span class="setting-label">Price Changes</span>
    <span class="toggle is-on" style="top:0"></span>
  </div>
  <div class="setting-row" style="top:390px;height:252px;padding-top:78px">
    <span class="setting-label">Petrol News &amp; Updates</span>
    <span class="toggle is-off" style="top:75px"></span>
  </div>
  <div class="setting-row" style="top:642px;height:242px;padding-top:74px">
    <span class="setting-label">Promos &amp; Deals</span>
    <span class="setting-hint">Get access to deals &amp; exclusive savings</span>
    <span class="toggle is-off" style="top:77px"></span>
  </div>
  <a class="back-button">
    <svg width="30" height="48" viewBox="0 0 30 48"><path d="M26 4L6 24l20 20" fill="none" stroke="#fff" stroke-width="6" stroke-linecap="round" stroke-linejoin="round"/></svg>
    Back
  </a>
</main>

<nav class="tab-bar">
  <svg class="tab" style="left:108px" width="72" height="76" viewBox="0 0 72 76" fill="#fff">
    <path d="M4 6a6 6 0 0 1 6-6h30a6 6 0 0 1 6 6v70H4z"/><rect x="12" y="8" width="26" height="22" rx="3" fill="#007aff"/>
    <path d="M50 10l10 10v44a4 4 0 0 1-8 0V40h-6v-6h10v30" fill="none" stroke="#fff" stroke-width="6"/>
  </svg>
  <svg class="tab" style="left:390px" width="62" height="72" viewBox="0 0 62 72" fill="#fff">
    <path d="M6 24h50l4 48H2z"/><path d="M19 28V14a12 12 0 0 1 24 0v14" fill="none" stroke="#fff" stroke-width="6"/>
  </svg>
  <svg class="tab" style="left:666px" width="60" height="70" viewBox="0 0 60 70" fill="#fff">
    <circle cx="30" cy="17" r="17"/><path d="M0 60a22 22 0 0 1 22-22h16a22 22 0 0 1 22 22v4a6 6 0 0 1-6 6H6a6 6 0 0 1-6-6z"/>
  </svg>
  <div class="tab-active">
    <svg width="66" height="66" viewBox="0 0 66 66" fill="#007aff">
      <path d="M28 0h10l2 9 7 3 8-5 7 7-5 8 3 7 9 2v10l-9 2-3 7 5 8-7 7-8-5-7 3-2 9H28l-2-9-7-3-8 5-7-7 5-8-3-7-9-2V28l9-2 3-7-5-8 7-7 8 5 7-3z"/>
      <circle cx="33" cy="33" r="15" fill="#fff"/><circle cx="33" cy="33" r="10"/><circle cx="33" cy="33" r="5" fill="#fff"/>
    </svg>
    Settings
  </div>
</nav>
</body>
</html>
```